Personal coach needs brochure design for inspirational essay about authenticity

Overview:
I want a beautiful brochure, 11”x17” that folds to 8-1/2”x11” with 4 pages. Think of it as an oversize greeting card.
• Front cover: photograph of a dancer and title with attribution of quote (Lumafold jpeg photo attached)
• Inside spread: Copy (Helena Brisk copy attached) with some appropriate illustration, based on cover photo
• Back cover: contact information, brief descriptive copy, two small photos (jpeg photo attached; see copy for direction)
Copy for front cover title, inside spread and back cover is attached in doc titled "Helena Brisk copy"

Purpose of brochure:
I'm a personal coach and once a year I produce a 4-page illustrated inspirational essay, which invites personal reflection on living a more mindful, meaningful life. Most people I send them to collect them. Someday in the future I'd like to put a collection of these essays into a coffee table book and also create a website for the collection, which is related to the personal coaching that I do.
I have the brochures printed hard copy. I have attached a few examples from previous years. Each has a unique design related to its theme.

Concept:
This year’s essay theme, “There will only ever be one you!” is based on a quote by Helena Brisk, a famous modern dancer. The complete quote, which appears in the copy, is about being true to one’s authentic self. The essay is not about dance, but because the author of the quote was a dancer who personified this theme of being unique to self, I have selected a photo of dance for the cover.

Design Guidance:
Front cover: One possibility is to expand the background color of the Lumafold photo so the photo seems to emerge from the background. But I am open to ideas. I think the photo is artsy enough as it is, but there may be other ways to treat it (e.g. special effects) that would also work. The title should appear somewhere. Make the attribution (--Helena Brisk) in smaller type than the title.

Inside Spread: There may be ways to borrow a design motif from the cover photo to make the inside spread more visually interesting, i.e., not just straight copy. I think it may be helpful to make the font size of the quote larger than the rest of the copy, but it has to be read in sequence. Or maybe it's printed in same size as copy, but then also repeated and displayed by itself in larger type.

Back cover: If you look at some of the other examples I’ve sent, you’ll see how the back cover is typically handled. I want a reduced version of the cover to be placed near the line that says "this is the 16th in a series.." Then, there’s a jpeg photo of Helena Brisk that should be placed next to the copy description of her.

Need extra days to review

```html
<!DOCTYPE html>
<html lang="en">
<head>
<meta charset="utf-8">
<title>There Will Only Ever Be One You! — Brochure</title>
<link rel="stylesheet" href="https://fonts.googleapis.com/css2?family=Bebas+Neue&family=Source+Sans+3:ital,wght@0,400;0,600;0,700;1,400;1,700&display=swap">
<style>
  :root {
    --backdrop: #a7a8ab;
    --paper: #ffffff;
    --paper-tint: #f6f6f6;
    --ink: #111111;
    --body-ink: #1e1e1e;
    --teal: #1a9e92;
    --rule-blue: #4aa9e6;
    --photo-light: #8a9096;
    --photo-mid: #5e656c;
    --photo-dark: #2f343a;
    --dress: #3c4a58;
    --photo-navy: #1c2233;
    --portrait-pale: #9c9a92;
  }
  * { box-sizing: border-box; margin: 0; padding: 0; }
  html, body { width: 1200px; height: 1200px; overflow: hidden; }
  body {
    background: var(--backdrop);
    position: relative;
    font-family: "Source Sans 3", "Myriad Pro", sans-serif;
    color: var(--body-ink);
    -webkit-font-smoothing: antialiased;
    -moz-osx-font-smoothing: grayscale;
    text-rendering: geometricPrecision;
  }
  .spread {
    position: absolute;
    left: 211px;
    width: 778px;
    height: 503px;
    background: var(--paper);
    overflow: hidden;
  }
  .spread--outside { top: 44px; }
  .spread--inside { top: 603px; }

  /* grayscale text rendering on small copy */
  .copy { will-change: transform; color: var(--body-ink); }

  .photo {
    position: absolute;
    background:
      radial-gradient(ellipse 45% 38% at 62% 58%, var(--dress) 0%, rgba(60,74,88,0) 100%),
      radial-gradient(ellipse 60% 50% at 40% 30%, var(--photo-light) 0%, rgba(138,144,150,0) 100%),
      linear-gradient(160deg, var(--photo-mid) 0%, var(--photo-dark) 100%);
  }

  /* Front cover */
  .cover-band {
    position: absolute; left: 0; top: 343px; width: 389px; height: 64px;
    background: var(--teal);
  }
  .cover-photo { left: 27px; top: 71px; width: 195px; height: 361px; }
  .cover-frame {
    position: absolute; left: 32px; top: 80px; width: 192px; height: 338px;
    border: 1px solid rgba(255,255,255,0.85);
  }
  .cover-divider {
    position: absolute; left: 224px; top: 343px; width: 2px; height: 64px;
    background: var(--paper);
  }
  .cover-title {
    position: absolute; left: 226px; top: 74px; width: 140px;
    font-family: "Bebas Neue", "Oswald", sans-serif;
    font-weight: 400;
    font-size: 62px; line-height: 55px; color: var(--ink);
    text-align: center; letter-spacing: 0.5px;
  }
  .cover-title__accent { color: var(--paper); display: block; margin-top: 3px; }
  .cover-attribution {
    position: absolute; left: 234px; top: 414px;
    font-size: 16px; letter-spacing: 2px; color: var(--ink);
  }

  /* Back cover */
  .back-thumb { left: 412px; top: 26px; width: 147px; height: 135px; }
  .back-heading {
    position: absolute; left: 576px; top: 28px;
    font-family: "Bebas Neue", "Oswald", sans-serif; font-weight: 400;
    font-size: 18px; line-height: 17px; color: var(--ink);
  }
  .back-details {
    position: absolute; left: 576px; top: 66px; width: 180px;
    font-size: 5.4px; line-height: 7px;
  }
  .back-details p { margin-bottom: 3px; }
  .back-details .lead { font-style: italic; }
  .back-details .copyright { font-weight: 700; font-size: 6px; }
  .back-rule {
    position: absolute; left: 559px; top: 160px; width: 197px; height: 1px;
    background: var(--rule-blue);
  }
  .portrait-photo {
    position: absolute;
    left: 412px; top: 173px; width: 92px; height: 92px;
    background:
      radial-gradient(ellipse 30% 40% at 50% 55%, var(--portrait-pale) 0%, rgba(156,154,146,0) 100%),
      linear-gradient(var(--photo-navy), var(--photo-navy));
  }
  .portrait-caption {
    position: absolute; left: 412px; top: 268px; width: 150px;
    font-size: 5px; line-height: 6px; font-style: italic;
  }
  .back-about {
    position: absolute; left: 412px; top: 296px; width: 343px;
    font-size: 7.9px; line-height: 10.7px; text-align: justify;
  }
  .back-about p { margin-bottom: 11px; }
  .back-about .label { color: var(--teal); font-weight: 700; font-style: italic; }

  /* Inside spread */
  .inside-left {
    position: absolute; left: 0; top: 0; width: 389px; height: 503px;
    background: var(--paper-tint);
  }
  .essay-column {
    position: absolute; top: 34px; width: 170px;
    font-size: 8.2px; line-height: 10.7px; text-align: justify;
  }
  .essay-column--one { left: 26px; }
  .essay-column--two { left: 207px; }
  .essay-column p { margin-bottom: 10.7px; }
  .essay-column p.tight { margin-bottom: 0; }
  .essay-quote {
    font-style: italic; text-align: center; font-size: 8.3px; line-height: 11.5px;
  }
  .inside-photo { left: 417px; top: 24px; width: 331px; height: 457px; }
</style>
</head>
<body>

<section class="spread spread--outside">
  <div class="cover-band"></div>
  <div class="photo cover-photo" role="img" aria-label="Photograph of a leaping dancer in a flowing dark satin dress against a grey textured backdrop"></div>
  <div class="cover-frame"></div>
  <div class="cover-divider"></div>
  <h1 class="cover-title">There<br>Will<br>Only<br>Ever<br>Be One<span class="cover-title__accent">You!</span></h1>
  <p class="cover-attribution">Helena Brisk</p>

  <div class="photo back-thumb" role="img" aria-label="Reduced version of the cover photograph of the leaping dancer"></div>
  <h2 class="back-heading">There Will Only<br>Ever Be One You!</h2>
  <div class="back-details copy">
    <p class="lead"><b>There Will Only Ever Be One You</b> is the 16th in a series of Labor Day essays inviting a moment of reflection on living a more mindful life.</p>
    <p>Ruth Calloway Dane, Ph.D.<br>Heron Hill House<br>18 Orchard Lane<br>Millbrook, Vermont 05999</p>
    <p>Mobile: 555-014-2287<br>email: rdane@mailpost.example</p>
    <p class="copyright">©2023</p>
  </div>
  <div class="back-rule"></div>
  <div class="portrait-photo" role="img" aria-label="Black and white photograph of Helena Brisk dancing in a sweeping pale dress"></div>
  <p class="portrait-caption copy">"Helena Brisk in Note to the World, No. 1" © The Clara Vane Archive</p>
  <div class="back-about copy">
    <p><span class="label">About Helena Brisk:</span> Born in 1894, Helena Brisk danced and taught for over 70 years. She is recognized as a primal artistic force of the 20th century, whose influence on modernity has been compared to Pablo Renard, Julian Voss, Ilya Marek, and Franklin Hale. Her themes dealt with the lives and conflicts of ordinary people, and she brought serious issues to the stage like war, poverty, intolerance and the injustices of slavery and treatment of Native Americans. Rebelling against conventions of the past, her dancing and choreography exposed the depths of human emotion through intense movements that were forceful, stark, angular, jagged, and percussive — startlingly unlike the formality of classical ballet, which she saw as antiquated.</p>
    <p><span class="label">About Photographer Clara Vane:</span> In 1935 Clara Vane saw a performance by modern dancer and choreographer Helena Brisk. Vane was so inspired by the dance performance that she introduced herself to Brisk, and the two artists began an artistic collaboration that lasted more than 60 years. Vane often photographed dancers in action, to capture the emotion behind their movement. Her artistic style was in line with Brisk's philosophy of dance. This photo from the dance, "Note to the World," is one of Vane's most famous photographs. The title of this work comes from an Emily Ashcroft poem, which inspired Brisk to create a dance performance based on Ashcroft's life.</p>
  </div>
</section>

<section class="spread spread--inside">
  <div class="inside-left">
    <div class="essay-column essay-column--one copy">
      <p>In the rural Ohio village where I grew up, one of the highlights of Sunday morning church service — in between congregational hymn singing and the preacher's sermon — was the "special selection," a musical performance by a parishioner. Typically, it was a vocalist or instrumental on piano, organ or violin. One Sunday, we were surprised by an unusual performance. A plump, buxom farm wife approached the pulpit, puckered up her lips and unexpectedly began to <i>whistle</i> the hymn <i>"The Old Hillside Cross."</i> As a 10-year-old, I found this hilarious as I tried to choke back my wide-eyed amazement and giggles.</p>
      <p>Despite the irreverence of my pre-adolescent reaction, this memory has stayed with me for decades as an iconic example of the wonderment of individual differences. Of the delight I find in witnessing someone express herself in sometimes surprising and even courageous ways. Of the marvel of beholding a person be truly authentic and uniquely original.</p>
      <p>Someone who personified the irrepressible impulse to express her individuality was the early 20th century dancer and choreographer Helena Brisk. A pioneer of modern dance, she threw tradition overboard and was inspired to dance in a way that was a radical departure from the formalized style and rigidly dictated forms of classical ballet. Brisk felt compelled to express the rawness and emotion of human experience in her dancing — not just present a form of pretty entertainment. Iconoclastically brilliant, she created a new language of dance, a revolutionary vocabulary of movement that electrified the stage, often creating a visceral response in the audience.</p>
    </div>
    <div class="essay-column essay-column--two copy">
      <p>In her biography of Brisk, her friend and equally talented choreographer Agnes Varela recalled that despite sensational reviews for her own innovative work in the Broadway musical <i>Meadowlark!</i>, Varela had a gnawing feeling that her work was only mediocre. Varela confessed her anxieties to Brisk who listened quietly and then responded, "There will only ever be one you!" Continuing, she added:</p>
      <p class="essay-quote">"There is a vitality, a life-force, an energy, a quickening that is translated through you into action. And because there is only one of you in all of time, this expression is unique. And if you block it, the world will not have it. It is not your business to determine how good it is nor how valuable nor how it compares with other expressions. It is your business to keep it yours clearly and directly, to keep the channel open. You have to keep open and aware directly to the urges that motivate you. Above all else, keep the channel open!"</p>
      <p class="tight">Brisk's wisdom reminds us that we must not hold back or judge our gifts. Although there may be moments when we doubt ourselves or when we worry that we're not good enough, our job is to be fearless and to "keep the channel open."</p>
      <p>Guard the precious miracle of your own uniqueness. Find that home-sweet-home feeling where you feel you are your most authentic self. There will only ever be one you! And importantly, respect the differences of others. Our world would be a drab, boring place if we all only whistled one tune.</p>
    </div>
  </div>
  <div class="photo inside-photo" role="img" aria-label="Large photograph of the leaping dancer with arms raised and satin dress billowing"></div>
</section>

</body>
</html>
```